A webite for an Urgent Care for children

We need a design for a new website for an Urgent care for kids. We are based in Atlanta, GA and provide quality after-hours and urgent care services for children. We will appreciate an innovative design that employs flash technology, especially on the Home page. We also want there to be a Contact Us form. There should also be a control panel with the ability for us to make quick and minor edits on the website as needed without requiring the services of an expert.

Target Market(s)

Parents, children, general audience

Industry/Entity Type

Healthcare

Coding

Coded - Design and coding required

Number of Pages Required

5+ page

Font styles to use
Sans Serif
Decorative

Colors
acd037
acd136
cadf82
eaf2ce
f6faec

Requirements
Must have
• Mobile devices website capable
• Link to social media, Facebook, twitter, etc
Nice to have
• Ability for customers to pay online.

```html
<!DOCTYPE html>
<html lang="en">
<head>
<meta charset="utf-8">
<title>Totspot Urgent Care</title>
<link rel="stylesheet" href="https://fonts.googleapis.com/css2?family=Lato:wght@400;700;900&family=Oswald:wght@400&display=swap">
<style>
:root{
  --page:#ececec;
  --white:#ffffff;
  --ink:#1d1d1d;
  --text:#333333;
  --red:#dd2a2a;
  --orange:#f7a11b;
  --yellow:#edcf1c;
  --green:#22a83a;
  --blue:#3157d2;
  --indigo:#4a16a6;
  --violet:#9b27b0;
}
*{margin:0;padding:0;box-sizing:border-box}
html,body{width:777px;height:1200px;overflow:hidden}
body{position:relative;background:var(--page);font-family:'Lato',sans-serif;color:var(--text)}
.sky{position:absolute;left:0;top:0;width:777px;height:322px;background:linear-gradient(180deg,#a9c8e8 0%,#c7dcf0 100%)}
.column{position:absolute;left:118px;top:322px;width:540px;height:878px;background:var(--white)}
.nav{position:absolute;top:24px;left:0;width:777px;font-family:'Oswald',sans-serif;font-weight:400;font-size:8.4px;color:#2a2a2a;text-transform:uppercase}
.nav a{position:absolute;top:0;height:22px;line-height:22px;color:inherit;text-decoration:none;white-space:nowrap}
.nav a.active{background:var(--red);color:var(--white);border-radius:11px;width:48px;text-align:center}
.brand{position:absolute;display:flex;align-items:center;gap:5px;font-family:'Lato',sans-serif;font-weight:900;color:var(--indigo);white-space:nowrap}
.brand .dot{display:block;border-radius:50%;background:var(--red)}
.brand-top{left:346px;top:26px;font-size:17px}
.brand-top .dot{width:12px;height:12px}
.hero{position:absolute;left:118px;top:88px;width:540px;height:218px;border-radius:90px 90px 0 0;background:linear-gradient(180deg,#8c7436 0%,#5e7a3e 38%,#3f8f46 62%,#55b444 100%)}
.rainbow{position:absolute;left:118px;top:306px;width:540px;height:16px;display:flex}
.rainbow span{flex:1}
.c1{background:var(--red)}.c2{background:var(--orange)}.c3{background:var(--yellow)}.c4{background:var(--green)}.c5{background:var(--blue)}.c6{background:var(--indigo)}.c7{background:var(--violet)}
.welcome-title{position:absolute;left:118px;top:349px;width:540px;text-align:center;font-weight:700;font-size:17px;color:var(--ink)}
.welcome-text{position:absolute;left:147px;top:408px;width:254px;font-size:10.8px;line-height:16.1px}
.welcome-text p+p{margin-top:16px}
.care-badge{position:absolute;left:446px;top:408px;width:176px;height:176px;border-radius:50%;background:#bfe6c3;display:flex;align-items:center;justify-content:center}
.care-badge .core{width:150px;height:150px;border-radius:50%;background:radial-gradient(circle,#21a534 60%,#58c067 100%)}
.care-badge .alert{position:absolute;left:12px;top:10px;width:40px;height:40px;border-radius:50%;background:var(--red);display:flex;align-items:center;justify-content:center}
.care-badge .clock{position:absolute;right:-14px;top:46px;width:54px;height:54px;border-radius:50%;background:var(--yellow);border:4px solid #f5e66b;display:flex;align-items:center;justify-content:center}
.band{position:absolute;left:118px;top:612px;width:540px;height:270px;background:var(--blue)}
.photo{position:absolute;left:146px;top:639px;width:216px;height:216px;border-radius:50%;border:4px solid var(--white);background:linear-gradient(135deg,#c9d6e6 0%,#8fb0d6 45%,#e6ecf4 100%)}
.band-text{position:absolute;left:392px;top:664px;width:239px;text-align:right;color:var(--white);font-size:10.8px;line-height:16.2px}
.band-text p+p{margin-top:16px}
.feature{position:absolute;top:926px;width:146px;text-align:center;font-size:10.8px;line-height:16px}
.feature .icon{width:80px;height:80px;border-radius:50%;margin:0 auto 25px;display:flex;align-items:center;justify-content:center}
.f-open{left:151px}.f-open .icon{background:var(--yellow)}
.f-pay{left:315px}.f-pay .icon{background:var(--indigo)}
.f-walk{left:480px}.f-walk .icon{background:var(--violet)}
.footer-rule{position:absolute;left:118px;top:1158px;width:378px;height:3px;display:flex}
.footer-rule span{flex:1}
.footer-nav{position:absolute;left:129px;top:1170px;font-size:6.6px;font-weight:700;color:#333;white-space:nowrap}
.footer-nav span{margin-right:7px}
.copyright{position:absolute;left:129px;top:1186px;font-size:5.6px;color:#777}
.brand-foot{left:524px;top:1158px;font-size:15px}
.brand-foot .dot{width:11px;height:11px}
</style>
</head>
<body>
<div class="sky"></div>
<div class="column"></div>

<nav class="nav">
  <a class="active" style="left:145px">Home</a>
  <a style="left:206px">About Us</a>
  <a style="left:253px">Our Services</a>
  <a style="left:315px">FAQ</a>
  <a style="left:450px">Office Forms</a>
  <a style="left:512px">Finance and Insurance</a>
  <a style="left:607px">Contact Us</a>
</nav>
<div class="brand brand-top"><span class="dot"></span>TOTSPOT</div>

<div class="hero" role="img" aria-label="Illustrated landscape of brown hills, pine trees, a blue lake and green meadows under white clouds"></div>
<div class="rainbow"><span class="c1"></span><span class="c2"></span><span class="c3"></span><span class="c4"></span><span class="c5"></span><span class="c6"></span><span class="c7"></span></div>

<h1 class="welcome-title">WELCOME TO TOTSPOT!</h1>
<div class="welcome-text">
  <p>Welcome to TOTSPOT Urgent Care, your after-hours pediatric urgent care. We are here when your little ones suddenly wake up sick or sustain an injury and you need immediate medical attention, but your regular doctor’s office is closed.</p>
  <p>We are unique in the services we provide and are an alternative when your child needs care after-hours to be treated by pediatricians who specialize in caring for children.</p>
</div>
<div class="care-badge" role="img" aria-label="Green badge illustration of a doctor with stethoscope, alert and clock symbols">
  <div class="core"></div>
  <div class="alert">
    <svg width="10" height="24" viewBox="0 0 10 24"><rect x="2" y="0" width="6" height="15" rx="3" fill="#fff"/><circle cx="5" cy="20.5" r="3" fill="#fff"/></svg>
  </div>
  <div class="clock">
    <svg width="30" height="30" viewBox="0 0 30 30"><circle cx="15" cy="15" r="12" fill="none" stroke="#fff" stroke-width="3.5"/><path d="M15 8 V15 H21" stroke="#fff" stroke-width="3" fill="none" stroke-linecap="round"/></svg>
  </div>
</div>

<section class="band"></section>
<div class="photo" role="img" aria-label="Photo of medical staff wheeling a child on a hospital bed"></div>
<div class="band-text">
  <p>We are available so you do not have to take your child to a crowded Emergency Room to be treated by providers who are not pediatricians and do not specialize in caring for children. And also save you from &nbsp;the high cost of an ER visit.</p>
  <p>Our services are quick and our medical professionals are ready to serve you in our clean, friendly and professional environment.</p>
</div>

<div class="feature f-open">
  <div class="icon">
    <svg width="50" height="40" viewBox="0 0 50 40">
      <path d="M25 4 L12 16 M25 4 L38 16" stroke="#222" stroke-width="2.4" fill="none"/>
      <circle cx="25" cy="4" r="2.5" fill="#222"/>
      <rect x="5" y="14" width="40" height="22" rx="2" fill="#fff" stroke="#222" stroke-width="2" transform="rotate(-8 25 25)"/>
      <text x="25" y="30" text-anchor="middle" font-family="Lato,sans-serif" font-weight="900" font-size="11" fill="#4a16a6" transform="rotate(-8 25 25)">OPEN</text>
    </svg>
  </div>
  We are open every day, late into the night and weekends.
</div>
<div class="feature f-pay">
  <div class="icon">
    <svg width="52" height="36" viewBox="0 0 52 36">
      <rect x="1" y="1" width="50" height="34" rx="3" fill="#3a8de0"/>
      <rect x="1" y="6" width="50" height="6" fill="#1c3f8a"/>
      <rect x="6" y="18" width="10" height="7" rx="1" fill="#f2c52c"/>
      <rect x="22" y="18" width="20" height="3" fill="#fff"/>
      <rect x="22" y="23" width="12" height="3" fill="#fff"/>
    </svg>
  </div>
  Cash-pay is welcome.<br>We also accept most insurances and credit cards.
</div>
<div class="feature f-walk">
  <div class="icon">
    <svg width="40" height="54" viewBox="0 0 40 54" aria-label="Walk-in icon">
      <circle cx="22" cy="6" r="5" fill="#edcf1c"/>
      <g stroke="#edcf1c" stroke-linecap="round" stroke-linejoin="round" fill="none">
        <path d="M19 15 L15 31" stroke-width="7"/>
        <path d="M15 31 L20 40 L20 51" stroke-width="5"/>
        <path d="M15 31 L10 41 L4 50" stroke-width="5"/>
        <path d="M19 16 L11 22 L8 28" stroke-width="4"/>
        <path d="M19 16 L25 23 L32 24" stroke-width="4"/>
      </g>
    </svg>
  </div>
  Walk-ins welcome.
</div>

<div class="footer-rule"><span class="c1"></span><span class="c2"></span><span class="c3"></span><span class="c4"></span><span class="c5"></span><span class="c6"></span><span class="c7"></span></div>
<div class="footer-nav"><span>Home</span><span>About Us</span><span>Our Services</span><span>Finance and Insurance</span><span>Office Forms</span><span>Contact Us</span><span>FAQ</span></div>
<div class="copyright">Totspot Urgent Care © 2016. All Rights Reserved.</div>
<div class="brand brand-foot"><span class="dot"></span>TOTSPOT</div>
</body>
</html>
```